Psychology Practice Brochure and Letterhead
Quiet Harbor Psychological Services
I will have a submission in very shortly.
Sorry for the omission of our business contact information:
26840 W. 93rd St., Suite 410
Denbury Glen, IL 60512
Phone/Fax: 708.519.2483
info@quietharborpsych.example
#2,#7 and #8
*****Please note that we have shortened the "what to expect" section and alphabetized the items under the "what we treat" section. The new wording has been uploaded and is in the brief, along with some pictures and quotes we would like you to incorporate.
Thank you so much for your hard work on our project! We really like the green curved lines of #8 because it ties all the sections together. Could you put the "do i need therapy" section on the left outside panel? Then, you can move the "what to expect" section to the middle section with a map. Also, we really like the different shades of blue that you put behind the different text sections of #2 because it makes it easier to read.Thanks
Hello designers! We are so excited about your creative ideas for the brochure.
*****Please note that we have changed the brochure wording slightly, so please edit the text in your submissions. The changes are as follows:
1) The bullet points under "What we treat" have now been alphabetized.
2)We have shortened the "what to expect" section so that it fits better with the map on the back page of the brochure. These changes are reflected in the uploaded file called "new brochure wording."
Hello designers. Please see our design brief, as we have recently uploaded photos for you to include in the brochure. Below are some quotes that we like. Feel free to include one or two in the brochure.
"A journey of a thousand miles begins with a single step." Wen Shaoli
"I am not what happens to me, I am what I choose to become." Emil Dorst
"Life is not about who you once were, it is about who you are right now, and the person you have the potential to become." Unknown
We have identified a number of photos and quotes from various sites that we might want to use, but don't want to buy them all in case they don't ultimately work in the design. Is it ok to upload them, but then buy them if they are used?
Drafts #2 and #5: Could you incorporate both blue and green?
draft #5: thank you for your submission. Could we see the design without the pictures of physicians in lab coats? Instead, we would like to see pictures of adults, children or families. Having some pictures of people looking unhappy, angry or stressed is fine along with happier pictures, as well. Any quotes about happiness or hopefulness would also be welcome.
draft #2: Thank you for your submission. Could you replace the picture of the older couple and replace it with children or teens? Also, could you show us another option for the layout on the interior? Or, another way of separating the sections that doesn't use the solid lines?
draft #1: Thank you for your submission. We like the way you've used blue and green throughout the brochure, and the addition of the tree was nice. Is there a way to reduce the quantity of brown used? Also, could you give us some additional variety in the pictures used, such as some in which the people are not jumping?
Do you have any website?
we need vector logo! please upload it!

```html
<!DOCTYPE html>
<html lang="en">
<head>
<meta charset="utf-8">
<title>Quiet Harbor Psychological Services – Brochure and Letterhead</title>
<link href="https://fonts.googleapis.com/css2?family=Open+Sans:wght@400;600;700;800&display=swap" rel="stylesheet">
<style>
  :root{
    --stage:#e4e2df;
    --paper:#ffffff;
    --blue:#1b6db3;
    --blue-deep:#0f4f8a;
    --blue-soft:#d7eaf6;
    --blue-mist:#eaf4fb;
    --green:#7dbf3b;
    --green-deep:#4e9a2a;
    --ink:#333a40;
    --ink-soft:#5d666e;
    --photo-warm:#c9b8a6;
    --photo-cool:#9fb3c2;
    --photo-field:#8fb66a;
  }
  *{box-sizing:border-box;margin:0;padding:0}
  html,body{width:1200px;height:773px;overflow:hidden}
  body{background:var(--stage);font-family:"Open Sans",Arial,sans-serif;color:var(--ink);position:relative}
  .sheet{position:absolute;background:var(--paper);box-shadow:0 4px 14px rgba(0,0,0,.25);overflow:hidden}
  .photo{position:absolute}
  .heading{font-weight:800;color:var(--blue);text-transform:uppercase;letter-spacing:.3px}
  .copy{font-size:5.6px;line-height:1.45;color:var(--ink-soft)}
  .brand{font-weight:700;color:var(--green-deep);line-height:1.05}
  .brand-dot{display:inline-block;border-radius:50%;background:var(--green);vertical-align:middle}

  /* ---------- Brochure back (inside spread) ---------- */
  .brochure-back{left:427px;top:144px;width:701px;height:300px}
  .back-left{position:absolute;left:0;top:0;width:236px;height:196px}
  .back-left .photo{left:0;top:0;width:236px;height:58px;background:linear-gradient(120deg,var(--photo-cool),var(--photo-warm))}
  .back-left .block{position:absolute;left:10px;width:216px}
  .back-left .philosophy{top:64px}
  .back-left .help{top:128px;padding-left:52px}
  .back-left .help .photo{left:0;top:0;width:46px;height:52px;background:linear-gradient(160deg,var(--photo-cool),#7f95a6)}
  .heading.small{font-size:8px;margin-bottom:3px}
  .back-mid{position:absolute;left:244px;top:0;width:200px}
  .back-mid .intro{padding:8px 6px 0 0}
  .back-mid .intro p{margin-bottom:5px}
  .back-mid .treat{position:absolute;top:126px;left:0;width:200px}
  .back-right .photo{left:452px;top:0;width:249px;height:150px;background:linear-gradient(135deg,var(--photo-warm),#8a7664 70%,var(--photo-cool))}
  .back-right .caption{position:absolute;left:460px;top:156px;width:230px}
  .problems{position:absolute;left:0;top:178px;width:701px;height:100px}
  .problems svg{position:absolute;left:0;top:0}
  .problems .title{position:absolute;left:248px;top:26px;font-size:6.4px;font-weight:800;color:#fff;letter-spacing:.3px}
  .problems ul{position:absolute;left:248px;top:40px;width:440px;list-style:none;columns:2;column-gap:18px}
  .problems li{font-size:5.6px;color:var(--ink);line-height:1.6;padding-left:7px;position:relative}
  .problems li::before{content:"";position:absolute;left:0;top:3px;width:3px;height:3px;background:var(--green);border-radius:50%}
  .site-bar{position:absolute;left:0;bottom:0;width:701px;height:22px;background:var(--blue);color:#fff;font-size:8px;font-weight:600;text-align:center;line-height:22px}

  /* ---------- Brochure front (outside spread) ---------- */
  .brochure-front{left:36px;top:540px;width:377px;height:209px}
  .panel{position:absolute;top:0;height:209px;width:125.6px}
  .panel-left{left:0}
  .panel-mid{left:125.6px}
  .panel-right{left:251.2px}
  .panel-left .heading{font-size:7px;position:absolute;left:6px;top:7px}
  .panel-left ul{position:absolute;left:6px;top:20px;width:112px;list-style:none}
  .panel-left li{font-size:5.2px;color:var(--ink-soft);line-height:1.5;padding-left:6px;position:relative;margin-bottom:2px}
  .panel-left li::before{content:"";position:absolute;left:0;top:2.6px;width:3px;height:3px;background:var(--blue)}
  .panel-left .photo{left:6px;top:68px;width:40px;height:48px;background:linear-gradient(150deg,var(--photo-cool),var(--photo-warm))}
  .panel-left .testimonial{position:absolute;left:52px;top:70px;width:68px}
  .panel-left .testimonial .heading{position:static;font-size:5.6px}
  .panel-left .contact{position:absolute;left:0;top:146px;width:125.6px;height:63px;background:var(--blue);color:#fff;padding:6px}
  .panel-left .contact .heading{position:static;color:#fff;font-size:5.8px;margin-bottom:3px}
  .panel-left .contact p{font-size:5px;line-height:1.5}
  .panel-mid{background:var(--blue-mist)}
  .panel-mid .heading{font-size:7px;position:absolute;left:6px;top:7px}
  .panel-mid .intro{position:absolute;left:6px;top:18px;width:114px}
  .panel-mid .photo{left:6px;top:54px;width:114px;height:60px;background:linear-gradient(180deg,#b9d3e6,var(--photo-warm))}
  .panel-mid .quote{position:absolute;left:6px;top:122px;width:114px;font-size:5.6px;font-style:normal;color:var(--blue-deep);line-height:1.4}
  .panel-mid .quote cite{display:block;font-style:normal;font-weight:700;margin-top:2px}
  .panel-mid .more{position:absolute;left:6px;top:158px;width:114px}
  .panel-right .brand-top{position:absolute;left:0;top:0;width:125.6px;height:36px;padding:6px 8px;background:var(--paper)}
  .panel-right .brand-top .brand{font-size:9px}
  .panel-right .brand-top .sub{font-size:4.6px;color:var(--blue);font-weight:700;margin-top:2px}
  .panel-right .photo{left:0;top:36px;width:125.6px;height:100px;background:linear-gradient(180deg,#bcd9f0 0%,#d9e9f4 45%,var(--photo-field) 75%,#6f9c4a 100%)}
  .panel-right .tagline{position:absolute;left:0;top:136px;width:125.6px;height:36px;background:var(--blue);color:#fff;padding:5px 8px;text-align:right}
  .panel-right .tagline .line1{font-size:8px;font-weight:600}
  .panel-right .tagline .line2{font-size:13px;font-weight:800;letter-spacing:.5px}
  .panel-right .brand-foot{position:absolute;left:0;top:172px;width:125.6px;height:37px;background:var(--blue-soft);padding:5px 8px}
  .panel-right .brand-foot .brand{font-size:7px}
  .panel-right .brand-foot .url{font-size:5px;color:var(--blue-deep);margin-top:3px}

  /* ---------- Letterhead ---------- */
  .letterhead{left:883px;top:504px;width:281px;height:245px}
  .letterhead .masthead{position:absolute;left:0;top:14px;width:281px;text-align:center}
  .letterhead .masthead .brand{font-size:13px}
  .letterhead .masthead .brand-dot{width:9px;height:9px;margin-right:4px}
  .letterhead .masthead .sub{font-size:5.6px;color:var(--blue);font-weight:700;margin-top:2px}
  .letterhead svg{position:absolute;left:0;bottom:0}
  .letterhead .footer{position:absolute;left:8px;bottom:6px;font-size:5px;color:#fff;line-height:1.45}
  .letterhead .footer-right{position:absolute;right:8px;bottom:6px;font-size:5px;color:#fff}
</style>
</head>
<body>

<!-- Brochure back -->
<section class="sheet brochure-back" aria-label="Brochure inside spread">
  <div class="back-left">
    <div class="photo" role="img" aria-label="Photo of a worried woman resting her head in her hand"></div>
    <div class="block philosophy">
      <h3 class="heading small">Philosophy</h3>
      <p class="copy">We believe every person can grow. Our team offers warm, practical care that helps clients build strength, insight and lasting change.</p>
    </div>
    <div class="block help">
      <div class="photo" role="img" aria-label="Photo of a child sitting alone"></div>
      <h3 class="heading small">How we help</h3>
      <p class="copy">Individual, couple and family sessions shaped around your goals.</p>
    </div>
  </div>

  <div class="back-mid">
    <div class="intro copy">
      <p>Our licensed psychologists use proven methods in a calm, private setting.</p>
      <p>Sessions are scheduled at times that suit busy families.</p>
    </div>
    <div class="treat">
      <h3 class="heading small">What we treat</h3>
      <p class="copy">We work with children, teens and adults facing many life challenges.</p>
    </div>
  </div>

  <div class="back-right">
    <div class="photo" role="img" aria-label="Photo of a stressed man sitting on a bed, a woman in the background"></div>
  </div>

  <div class="problems">
    <svg width="701" height="100" viewBox="0 0 701 100" aria-hidden="true">
      <path d="M0 30 C180 0 420 0 701 14 L701 100 L0 100 Z" fill="var(--blue-soft)"/>
      <path d="M236 18 C380 4 560 4 701 12 L701 34 L236 34 Z" fill="var(--green)"/>
      <path d="M0 34 C180 6 420 2 701 10" fill="none" stroke="var(--green-deep)" stroke-width="2"/>
    </svg>
    <div class="title">SOME SPECIFIC PROBLEMS THAT WE CAN HELP WITH ARE</div>
    <ul>
      <li>Anxiety</li>
      <li>Attention problems</li>
      <li>Behavior concerns</li>
      <li>Depression</li>
      <li>Grief and loss</li>
      <li>Life transitions</li>
      <li>Parenting stress</li>
      <li>Relationship issues</li>
      <li>School difficulties</li>
      <li>Self-esteem</li>
      <li>Sleep problems</li>
      <li>Stress management</li>
    </ul>
  </div>
  <div class="site-bar">www.quietharbor.example</div>
</section>

<!-- Brochure front -->
<section class="sheet brochure-front" aria-label="Brochure outside spread">
  <div class="panel panel-left">
    <h3 class="heading">Do I Need Therapy?</h3>
    <ul>
      <li>Feeling sad or worried most days</li>
      <li>Trouble at school or work</li>
      <li>Conflict at home</li>
      <li>Changes in sleep or appetite</li>
    </ul>
    <div class="photo" role="img" aria-label="Photo of a thoughtful teenager"></div>
    <div class="testimonial">
      <h4 class="heading">Testimonials</h4>
      <p class="copy">“Caring, patient and truly helpful.”</p>
    </div>
    <div class="contact">
      <h4 class="heading">Learn more about us</h4>
      <p>26840 W. 93rd St., Suite 410<br>Denbury Glen, IL 60512<br>Phone/Fax: 708.519.2483<br>info@quietharborpsych.example</p>
    </div>
  </div>

  <div class="panel panel-mid">
    <h3 class="heading">What to expect</h3>
    <p class="copy intro">Your first visit includes a relaxed talk about your concerns and goals.</p>
    <div class="photo" role="img" aria-label="Photo of a smiling mother and child"></div>
    <blockquote class="quote">“A journey of a thousand miles begins with a single step.”<cite>Wen Shaoli</cite></blockquote>
    <p class="copy more">Together we build a plan that fits you.</p>
  </div>

  <div class="panel panel-right">
    <div class="brand-top">
      <div class="brand"><span class="brand-dot" style="width:7px;height:7px;margin-right:3px"></span>Quiet Harbor</div>
      <div class="sub">Psychological Services</div>
    </div>
    <div class="photo" role="img" aria-label="Photo of a happy family with a child on a father's shoulders in a field"></div>
    <div class="tagline">
      <div class="line1">For a better</div>
      <div class="line2">TOMORROW</div>
    </div>
    <div class="brand-foot">
      <div class="brand">Quiet Harbor Psychological Services</div>
      <div class="url">www.quietharbor.example</div>
    </div>
  </div>
</section>

<!-- Letterhead -->
<section class="sheet letterhead" aria-label="Letterhead">
  <div class="masthead">
    <div class="brand"><span class="brand-dot"></span>Quiet Harbor</div>
    <div class="sub">Psychological Services</div>
  </div>
  <svg width="281" height="70" viewBox="0 0 281 70" aria-hidden="true">
    <path d="M0 40 C90 20 190 18 281 6 L281 70 L0 70 Z" fill="var(--blue)"/>
    <path d="M0 36 C90 14 190 12 281 0 L281 8 C190 20 90 24 0 44 Z" fill="var(--green)"/>
    <path d="M0 30 C100 8 200 6 281 -4" fill="none" stroke="var(--blue-soft)" stroke-width="1.5"/>
  </svg>
  <div class="footer">26840 W. 93rd St., Suite 410<br>Denbury Glen, IL 60512 · 708.519.2483</div>
  <div class="footer-right">www.quietharbor.example</div>
</section>

</body>
</html>
```